Lanterns Over Glass - CD 4Panel Digipack

Looking for a great cover for my 2nd EP. Titled Lanterns Over Glass an inspirational track about following your goals however also some high tempo dance numbers. No idea what concept we are after. Looking for something with great ideas. It's a 4 panel digipack design.Open to concept ideas. Front cover will feature black and white photo but the rest is completely up to designer. Looking forward to ideas I haven't thought of.
Target Market(s)
Teenagers
Industry/Entity Type
Music Download
Colors
Designer to choose colors to be used in the design.
Requirements
Must have
- At least one of the photos attached

```html
<!DOCTYPE html>
<html lang="en">
<head>
<meta charset="utf-8">
<title>Rory Calloway – Lanterns Over Glass – Back Panel</title>
<link rel="stylesheet" href="https://fonts.googleapis.com/css2?family=Montserrat:wght@700;800&family=Barlow:wght@300;400&display=swap">
<style>
  :root {
    --bg-dark: #6f5048;
    --bg-mid: #8c6b60;
    --bg-light: #9b7b6f;
    --accent: #fcc62d;
    --ink-light: #ffffff;
    --ink-dark: #3a2a22;
    --photo-a: #c9b7a4;
    --photo-b: #5c4a3e;
  }
  * { margin: 0; padding: 0; box-sizing: border-box; }
  html, body { width: 1200px; height: 953px; overflow: hidden; }
  body { font-family: "Montserrat", sans-serif; }

  .panel {
    position: relative;
    width: 1200px; height: 953px;
    overflow: hidden;
    background:
      radial-gradient(ellipse at 70% 30%, var(--bg-light) 0%, transparent 60%),
      linear-gradient(160deg, var(--bg-mid) 0%, var(--bg-dark) 100%);
  }

  .artist-photo {
    position: absolute;
    left: 128px; top: 60px;
    width: 576px; height: 893px;
    background: radial-gradient(ellipse at 50% 35%, var(--photo-a) 0%, var(--photo-b) 75%);
    border-radius: 260px 260px 0 0;
    opacity: 0.85;
  }

  .spine {
    position: absolute;
    top: 476px;
    white-space: nowrap;
    font-weight: 800;
    font-size: 22px;
    letter-spacing: 0.5px;
    line-height: 1;
  }
  .spine .artist { color: var(--accent); margin-right: 14px; }
  .spine .title { color: var(--ink-light); }
  .spine-left { left: 56px; transform: translate(-50%, -50%) rotate(-90deg); }
  .spine-right { left: 1154px; transform: translate(-50%, -50%) rotate(90deg); }

  .track-bar {
    position: absolute;
    left: 1058px; top: 0;
    width: 28px; height: 294px;
    background: var(--accent);
  }

  .tracklist { position: absolute; right: 156px; top: 0; width: 600px; }
  .track {
    position: absolute; right: 0;
    transform: translateY(-50%);
    white-space: nowrap;
    color: var(--ink-light);
    font-weight: 800;
    font-size: 28px;
    line-height: 1;
  }
  .track.feature {
    font-family: "Barlow", sans-serif;
    font-weight: 300;
    font-size: 29px;
  }
  .track-no {
    position: absolute; left: 1058px; width: 28px;
    transform: translateY(-50%);
    text-align: center;
    font-family: "Barlow", sans-serif;
    font-weight: 300;
    font-size: 25px;
    color: var(--ink-dark);
    line-height: 1;
  }

  .credits { position: absolute; right: 112px; top: 0; width: 700px; }
  .credit-line {
    position: absolute; right: 0;
    transform: translateY(-50%);
    white-space: nowrap;
    font-family: "Barlow", sans-serif;
    font-weight: 400;
    font-size: 18px;
    color: var(--ink-light);
    letter-spacing: 0.3px;
    line-height: 1;
  }
  .credit-line b {
    font-family: "Montserrat", sans-serif;
    font-weight: 800;
    font-size: 17px;
    color: var(--accent);
    letter-spacing: 0;
  }

  .legal {
    position: absolute; right: 114px; top: 827px;
    text-align: right;
    font-family: "Barlow", sans-serif;
    font-size: 10px;
    line-height: 13.5px;
  }
  .legal-line {
    display: inline-block;
    background: var(--accent);
    color: var(--ink-dark);
    line-height: 13.5px;
    padding: 0 3px;
    vertical-align: top;
  }
  .website {
    position: absolute;
    left: 978px; top: 884px;
    width: 108px; height: 19px;
    background: var(--accent);
    color: var(--ink-dark);
    font-family: "Barlow", sans-serif;
    font-size: 10px;
    line-height: 19px;
    text-align: center;
  }
</style>
</head>
<body>
<main class="panel">
  <div class="artist-photo" role="img" aria-label="Sepia portrait photo of the young artist in a dark t-shirt holding a cream electric guitar"></div>

  <div class="spine spine-left"><span class="artist">RORY CALLOWAY</span><span class="title">LANTERNS OVER GLASS</span></div>
  <div class="spine spine-right"><span class="artist">RORY CALLOWAY</span><span class="title">LANTERNS OVER GLASS</span></div>

  <div class="track-bar"></div>
  <div class="tracklist">
    <div class="track" style="top:76px">NEON PAPER SKYLINES</div>
    <div class="track" style="top:108px">LANTERNS OVER GLASS</div>
    <div class="track" style="top:140px">AFTERGLOW</div>
    <div class="track feature" style="top:173px">(WITH MARA QUINLAN)</div>
    <div class="track" style="top:206px">SATURN DAYS</div>
    <div class="track" style="top:238px">SPIN AROUND</div>
    <div class="track" style="top:270px">HOMEWARD</div>
  </div>
  <div class="track-no" style="top:77px">1</div>
  <div class="track-no" style="top:109px">2</div>
  <div class="track-no" style="top:141px">3</div>
  <div class="track-no" style="top:207px">4</div>
  <div class="track-no" style="top:239px">5</div>
  <div class="track-no" style="top:271px">6</div>

  <div class="credits">
    <div class="credit-line" style="top:340px"><b>NEON PAPER SKYLINES, LANTERNS OVER GLASS,</b></div>
    <div class="credit-line" style="top:362px"><b>AFTERGLOW, SATURN DAYS</b> AND <b>HOMEWARD</b></div>
    <div class="credit-line" style="top:385px">WRITTEN BY <b>RORY CALLOWAY</b></div>

    <div class="credit-line" style="top:430px"><b>SPIN AROUND</b> WRITTEN BY <b>RORY CALLOWAY</b></div>
    <div class="credit-line" style="top:453px">AND <b>THEO BRANDT ELLIS</b></div>

    <div class="credit-line" style="top:496px"><b>NEON PAPER SKYLINES, LANTERNS OVER GLASS,</b></div>
    <div class="credit-line" style="top:518px"><b>SATURN DAYS</b> AND <b>HOMEWARD</b></div>
    <div class="credit-line" style="top:541px">PRODUCED BY <b>VELVET ENGINE</b></div>

    <div class="credit-line" style="top:584px"><b>AFTERGLOW</b></div>
    <div class="credit-line" style="top:606px">PRODUCED BY <b>OWEN MARSH</b></div>

    <div class="credit-line" style="top:650px"><b>SPIN AROUND</b></div>
    <div class="credit-line" style="top:672px">PRODUCED BY <b>THEO BRANDT ELLIS</b></div>
  </div>

  <div class="legal">
    <span class="legal-line">© 2017 Rory Calloway</span><br>
    <span class="legal-line">All rights reserved. Unauthorized duplication is a violation of applicable laws.</span><br>
    <span class="legal-line">Manufactured in USA</span>
  </div>
  <div class="website">www.rorycalloway.com</div>
</main>
</body>
</html>
```